Website redesign

We've inherited a Tilecraft Website that we'd like to change to a Pagemill website to match our other sites.

Site I want redesigned is: https://www.corvellawings.com/
which will change to www.corvellaskytours.com.au

Our other websites I want it to match:
https://marloweskytours.com.au/
https://penfaricays.au/
https://tindaleskytours.com.au/
https://brightvalewings.com.au/

I do not want the design to deviate too much from the others, the main difference will be colours that need to align with the logo I've uploaded.

Pages I want:
Home
About Us
Gallery
News/Blog
Overflies
Half Day Tours
Full Day Tours
Transfers
Contact

Other pages will link to the other website - like on the other websites currently

```html
<!DOCTYPE html>
<html lang="en">
<head>
<meta charset="utf-8">
<title>Corvella Sky Tours</title>
<link href="https://fonts.googleapis.com/css2?family=Poppins:wght@300;400;500;600;700;800&family=Open+Sans:wght@400;600&display=swap" rel="stylesheet">
<style>
:root{
  --blue:#4f9fd2;
  --orange:#c45a2a;
  --green:#8dbf3f;
  --navy:#1d3151;
  --ink:#1b1b1b;
  --grey:#6b6b6b;
  --pale:#eef6fc;
  --white:#fff;
}
*{box-sizing:border-box;margin:0;padding:0}
html,body{width:1200px;height:3576px;overflow:hidden}
body{font-family:"Open Sans",sans-serif;color:var(--ink);background:var(--white);position:relative}
.sec{position:relative;width:1200px;overflow:hidden}
.abs{position:absolute}
.btn{display:inline-flex;align-items:center;gap:8px;background:var(--orange);color:#fff;font-family:"Poppins",sans-serif;font-weight:600;font-size:15px;padding:0 24px;height:44px;border-radius:4px;text-decoration:none;white-space:nowrap}
.btn.ghost{background:transparent;border:2px solid #fff}
.photo{position:absolute}
/* top bar */
.topbar{height:28px;background:var(--blue);color:#fff;font-size:12px}
.topbar span{position:absolute;top:6px;white-space:nowrap}
.dot{display:inline-block;width:10px;height:10px;border-radius:50%;background:#fff;margin-left:5px;vertical-align:-1px}
/* nav */
.nav{height:76px;background:#fff;box-shadow:0 1px 4px rgba(0,0,0,.08)}
.brand{position:absolute;left:118px;top:20px;display:flex;align-items:center;gap:10px;font-family:"Poppins",sans-serif;font-size:20px;font-weight:500;color:var(--blue)}
.brand i{width:34px;height:34px;border-radius:50%;background:var(--blue);display:block}
.menu a{position:absolute;top:29px;font-family:"Open Sans",sans-serif;font-size:14px;color:var(--ink);text-decoration:none;white-space:nowrap}
.menu a.on{color:var(--green)}
.nav .btn{position:absolute;left:974px;top:21px;height:36px;font-size:14px;padding:0 20px}
/* hero */
.hero{height:536px;background:linear-gradient(100deg,#3f8d9f 0%,#6aa3a5 35%,#b9683e 60%,#a84f29 100%)}
.hero h1{position:absolute;width:100%;text-align:center;font-family:"Poppins",sans-serif;color:#fff;font-size:53px;line-height:73px;top:112px;font-weight:300;letter-spacing:.5px}
.hero h1 b{font-weight:800}
.hero .ctas{position:absolute;top:289px;width:100%;display:flex;justify-content:center;gap:24px}
.hero .ctas .btn{height:47px;font-size:16px}
.arrow{position:absolute;top:222px;width:37px;height:37px;border-radius:50%;display:flex;align-items:center;justify-content:center}
/* about */
.about{height:638px}
.title{font-family:"Poppins",sans-serif;font-size:36px;font-weight:300;line-height:48px;color:var(--ink);white-space:nowrap}
.title b{font-weight:700}
.text{font-size:14px;line-height:24px;color:var(--grey)}
/* excursions */
.excursions{height:808px;background:var(--pale)}
.card{position:absolute;width:296px;height:319px;display:flex;flex-direction:column;justify-content:flex-end;align-items:center;padding-bottom:14px;color:#fff;font-family:"Poppins",sans-serif;font-size:18px}
.card small{font-size:12px;margin-top:6px}
.card.feature{background:var(--green);justify-content:center;padding:0 24px;text-align:center}
.circ{position:absolute;top:300px;width:57px;height:57px;border-radius:50%;display:flex;flex-direction:column;align-items:center;justify-content:center;font-size:11px;font-family:"Poppins",sans-serif}
/* stats */
.stats{height:327px;background:linear-gradient(180deg,#1c3050 0%,#25406a 55%,#3a4d5e 80%,#2a3a55 100%)}
.stat{position:absolute;display:flex;align-items:center;color:#fff}
.stat .rule{width:1px;height:62px;background:rgba(255,255,255,.6);margin:0 20px}
.stat strong{display:block;font-family:"Poppins",sans-serif;font-size:40px;font-weight:700;color:var(--green);line-height:46px}
.stat span{font-size:14px}
/* clients */
.clients{height:387px}
.review{position:absolute;top:140px;width:285px;height:209px;background:#fff;box-shadow:0 2px 10px rgba(0,0,0,.1);padding:20px 18px}
.review p{font-size:12px;line-height:23px;color:var(--grey)}
.who{display:flex;align-items:center;gap:12px;margin-top:18px}
.who i{width:55px;height:55px;border-radius:50%;display:flex;align-items:center;justify-content:center;color:#fff;font-style:normal;font-family:"Poppins",sans-serif;font-weight:700;font-size:26px}
.who b{display:block;font-weight:500;font-family:"Poppins",sans-serif;font-size:16px}
.stars{color:#f2b01e;font-size:11px;letter-spacing:1px}
.ago{position:absolute;right:12px;bottom:12px;font-size:9px;color:#aaa}
/* booking */
.booking{height:445px}
.booking .title{font-size:32px}
/* footer */
.footer{height:336px;background:var(--navy);color:#fff}
.footer h4{font-family:"Poppins",sans-serif;font-weight:400;font-size:18px}
.footer ul{list-style:none;font-size:14px;line-height:24px}
.soc{width:27px;height:27px;border-radius:50%;border:1.5px solid #fff;display:inline-block;margin:0 5px}
</style>
</head>
<body>

<header class="sec topbar">
  <span style="left:600px">✉ info@brightvalewings.au</span>
  <span style="left:812px">☎ 08 5550 0142</span>
  <span style="left:943px">Follow Us: <i class="dot"></i><i class="dot"></i><i class="dot"></i></span>
</header>

<nav class="sec nav">
  <div class="brand"><i></i>Corvella</div>
  <div class="menu">
    <a class="on" href="#" style="left:344px">Home</a>
    <a href="#" style="left:412px">About Us</a>
    <a href="#" style="left:501px">Half Day Tours</a>
    <a href="#" style="left:627px">Full Day Tours</a>
    <a href="#" style="left:750px">Transfers</a>
    <a href="#" style="left:840px">Gallery</a>
    <a href="#" style="left:914px">Blog</a>
  </div>
  <a class="btn" href="#">CONTACT</a>
</nav>

<section class="sec hero" role="img" aria-label="Aerial photo of red coastal cliffs meeting turquoise sea">
  <h1><b>SCENIC FLIGHTS –</b> DAY TOURS<br>CHARTER <b>– AIRWORK</b></h1>
  <div class="ctas"><a class="btn" href="#">BOOK NOW ›</a><a class="btn ghost" href="#">CONTACT US ›</a></div>
  <div class="arrow" style="left:79px;background:#fff"><svg width="12" height="12" viewBox="0 0 12 12"><path d="M8 1 3 6l5 5" stroke="#333" stroke-width="2" fill="none"/></svg></div>
  <div class="arrow" style="left:1084px;background:var(--green)"><svg width="12" height="12" viewBox="0 0 12 12"><path d="M4 1l5 5-5 5" stroke="#fff" stroke-width="2" fill="none"/></svg></div>
  <svg class="abs" style="left:590px;top:460px" width="20" height="46" viewBox="0 0 20 46"><rect x="2" y="1" width="16" height="26" rx="8" fill="none" stroke="#fff" stroke-width="1.5"/><line x1="10" y1="7" x2="10" y2="12" stroke="#fff" stroke-width="1.5"/><path d="M10 31v12M6 39l4 4 4-4" stroke="#fff" stroke-width="1.5" fill="none"/></svg>
</section>

<section class="sec about">
  <div class="abs" style="left:104px;top:58px;width:292px;height:303px;background:var(--blue)"></div>
  <div class="photo" style="left:144px;top:97px;width:260px;height:249px;background:linear-gradient(#58a9d4,#d98a3a)" role="img" aria-label="Tour group waving on a beach"></div>
  <div class="photo" style="left:404px;top:97px;width:114px;height:249px;background:linear-gradient(#2a1408,#a2421a)" role="img" aria-label="Campfire at night"></div>
  <div class="photo" style="left:144px;top:346px;width:260px;height:224px;background:linear-gradient(#3a86c8,#c2632e)" role="img" aria-label="Walkers on a red dune above the sea"></div>
  <div class="photo" style="left:404px;top:346px;width:114px;height:127px;background:linear-gradient(#7fb0d6,#d7b07a)" role="img" aria-label="Sandy coastal dunes"></div>
  <div class="photo" style="left:404px;top:473px;width:260px;height:97px;background:linear-gradient(#d8a56e,#c98a50)" role="img" aria-label="Group walking across sand dunes"></div>
  <div class="abs" style="left:557px;top:130px;width:492px">
    <h2 class="title"><b>ABOUT</b> US</h2>
    <p class="text" style="margin-top:18px;text-align:justify">Corvella Sky Tours Flight Crew Are Trained To The Highest Standard. Our Commitment To Safety And Service Make Us One Of The Highly Regarded Charter Services In Wa.</p>
    <p class="text" style="margin-top:10px;text-align:justify">Duis aute irure dolor in reprehenderit in voluptate velit esse cillum dolore eu fugiat nulla pariatur. Excepteur sint occaecat cupidatat non proident, sunt in culpa qui officia deserunt mollit anim id est laborum.</p>
    <a class="btn" href="#" style="margin-top:32px">READ MORE ›</a>
  </div>
</section>

<section class="sec excursions">
  <div class="abs" style="left:143px;top:114px;width:280px">
    <h2 class="title"><b>EXPLORE OUR</b><br>EXCURSIONS</h2>
    <p class="text" style="margin-top:18px">Duis aute irure dolor in reprehenderit in voluptate velit esse cillum dolore</p>
  </div>
  <div class="circ" style="left:143px;border:1px solid #333">PREV<span>‹</span></div>
  <div class="circ" style="left:211px;background:var(--green);color:#fff">NEXT<span>›</span></div>
  <div class="card" style="left:453px;top:76px;background:linear-gradient(#6f8fa8,#3b3326)" role="img" aria-label="Tour group in front of a four wheel drive">Full Day Tours<small>⌃</small></div>
  <div class="card" style="left:760px;top:76px;background:linear-gradient(135deg,#4a86b0,#c4653a 60%,#2b5b88)" role="img" aria-label="Swimmers splashing in the sea below red cliffs">Half Day Tours<small>⌃</small></div>
  <div class="card" style="left:146px;top:407px;background:linear-gradient(#3d7fb8,#c27a4a)" role="img" aria-label="Family posing on red sand">Custom Tours<small>⌃</small></div>
  <div class="card feature" style="left:453px;top:407px">
    <svg width="64" height="60" viewBox="0 0 64 60" fill="none" stroke="#fff" stroke-width="2"><circle cx="24" cy="30" r="20"/><path d="M24 4c-6 0-10 5-10 10 0 7 10 16 10 16s10-9 10-16c0-5-4-10-10-10z"/><rect x="36" y="34" width="24" height="20" rx="2"/><path d="M42 34v-4h12v4M36 44h24"/></svg>
    <div style="margin-top:10px">Transfers</div>
    <p style="font-family:'Open Sans',sans-serif;font-size:13px;line-height:23px;margin-top:10px">Lorem ipsum dolor sit amet, consectetur adipiscing elit, sed do eiusmod tempor incididunt ut labore et dolore</p>
    <a class="btn" href="#" style="margin-top:18px">LEARN MORE ›</a>
  </div>
  <div class="card" style="left:760px;top:407px;background:linear-gradient(#3a3f4c,#c98a3c 55%,#2a3b55)" role="img" aria-label="Passenger aircraft flying over a bay at sunset">Overflies<small>⌃</small></div>
</section>

<section class="sec stats" role="img" aria-label="Dark blue tinted aerial coast photo">
  <div class="stat" style="left:292px;top:70px"><svg width="66" height="66" viewBox="0 0 66 66" fill="none" stroke="var(--blue)" stroke-width="2"><circle cx="33" cy="33" r="30"/><path d="M8 24h50M8 42h50M33 3c-10 12-10 48 0 60M33 3c10 12 10 48 0 60"/></svg><div class="rule"></div><div><strong>14 +</strong><span>Scenic Fights &amp; Charters</span></div></div>
  <div class="stat" style="left:672px;top:70px"><svg width="66" height="66" viewBox="0 0 66 66" fill="none" stroke="var(--blue)" stroke-width="2"><circle cx="14" cy="14" r="6"/><path d="M2 62l20-34 12 18 10-14 20 30z"/></svg><div class="rule"></div><div><strong>40 +</strong><span>Scenic Trips</span></div></div>
  <div class="stat" style="left:292px;top:193px"><svg width="66" height="66" viewBox="0 0 66 66" fill="none" stroke="var(--blue)" stroke-width="2"><circle cx="33" cy="40" r="22"/><path d="M24 4c-6 0-10 4-10 10 0 7 10 16 10 16s10-9 10-16c0-6-4-10-10-10z"/></svg><div class="rule"></div><div><strong>14 +</strong><span>Destinations</span></div></div>
  <div class="stat" style="left:672px;top:193px"><svg width="66" height="66" viewBox="0 0 66 66" fill="none" stroke="var(--blue)" stroke-width="2"><circle cx="20" cy="14" r="7"/><circle cx="46" cy="14" r="7"/><circle cx="33" cy="10" r="6"/><path d="M6 40c0-10 6-16 14-16s14 6 14 16M32 40c0-10 6-16 14-16s14 6 14 16M10 50l14 10h18l14-10"/></svg><div class="rule"></div><div><strong>2500 +</strong><span>Happy Customers</span></div></div>
</section>

<section class="sec clients">
  <h2 class="title abs" style="width:100%;text-align:center;top:62px"><b>WHAT</b> CLIENTS <b>SAY</b></h2>
  <svg class="abs" style="left:113px;top:230px" width="14" height="24" viewBox="0 0 14 24"><path d="M12 2 2 12l10 10" stroke="#444" stroke-width="2" fill="none"/></svg>
  <svg class="abs" style="left:1071px;top:230px" width="14" height="24" viewBox="0 0 14 24"><path d="M2 2l10 10-10 10" stroke="#444" stroke-width="2" fill="none"/></svg>
  <div class="review" style="left:146px"><p>Lorem ipsum dolor sit amet, consectetur adipiscing elit, sed do eiusmod tempor incididunt ut labore et dolore magna aliqua. Ut enim ad minim</p><div class="who"><i style="background:#1d2a5c">M</i><div><b>Mira Lethbridge</b><span class="stars">★★★★★</span></div></div><span class="ago">2 months ago</span></div>
  <div class="review" style="left:457px"><p>Lorem ipsum dolor sit amet, consectetur adipiscing elit, sed do eiusmod tempor incididunt ut labore et dolore magna aliqua. Ut enim ad minim</p><div class="who"><i style="background:#5a3d36">K</i><div><b>Kato-RVL</b><span class="stars">★★★★★</span></div></div><span class="ago">2 months ago</span></div>
  <div class="review" style="left:770px"><p>Lorem ipsum dolor sit amet, consectetur adipiscing elit, sed do eiusmod tempor incididunt ut labore et dolore magna aliqua. Ut enim ad minim</p><div class="who"><i style="background:#0f4a3a">D</i><div><b>Dylan Oakes</b><span class="stars">★★★★★</span></div></div><span class="ago">2 months ago</span></div>
</section>

<section class="sec booking">
  <div class="abs" style="left:0;top:104px;width:364px;height:341px;background:var(--blue)"></div>
  <div class="photo" style="left:144px;top:47px;width:441px;height:345px;background:linear-gradient(120deg,#8fc1e0,#d99a66 50%,#b5473a)" role="img" aria-label="Smiling couple taking a selfie beside a passenger aircraft"></div>
  <div class="abs" style="left:643px;top:100px;width:420px">
    <h2 class="title">BOOKING <b>ARE AVAILABLE</b></h2>
    <p class="text" style="margin-top:18px">We Are Available Business Hours To Take Your Call For What Ever The Question May Be! If You Require A Quote Or Need Further Information About Our Services, Please Send Us An E-mail!</p>
    <a class="btn" href="#" style="margin-top:32px">BOOK NOW ›</a>
  </div>
</section>

<footer class="sec footer">
  <div class="brand" style="left:143px;top:104px;font-size:24px"><i style="width:40px;height:40px"></i>Corvella</div>
  <div class="abs" style="left:482px;top:52px">
    <h4>LINKS</h4>
    <div style="display:flex;gap:60px;margin-top:8px">
      <ul><li>Home</li><li>About Us</li><li>Gallery</li><li>Blog</li><li>Overflies</li></ul>
      <ul><li>Half Day Tours</li><li>Full Day Tours</li><li>Transfers</li><li>Contact</li></ul>
    </div>
  </div>
  <div class="abs" style="left:845px;top:52px">
    <h4>CONTACT US</h4>
    <p style="font-size:14px;margin-top:14px;display:flex;align-items:center;gap:10px"><i class="dot" style="width:22px;height:22px;background:var(--blue);margin:0"></i>08 5550 0142</p>
    <p style="font-size:14px;margin-top:14px;display:flex;align-items:center;gap:10px"><i class="dot" style="width:22px;height:22px;background:var(--blue);margin:0"></i>info@brightvalewings.au</p>
  </div>
  <div class="abs" style="left:143px;top:225px;width:913px;height:1px;background:rgba(255,255,255,.25)"></div>
  <p class="abs" style="width:100%;text-align:center;top:244px;font-size:13px">Copyright© 2025 Corvella Sky Tours &nbsp;|&nbsp; All Rights Reserved</p>
  <div class="abs" style="width:100%;text-align:center;top:282px"><i class="soc"></i><i class="soc" style="background:var(--green);border-color:var(--green)"></i><i class="soc"></i></div>
</footer>

</body>
</html>
```